Eye catching Stationary Design

Healthcare consultant firm looking for stationary design ( letterhead, envelope and business cards) That’s professional, classy and eye catching . The design should incorporate the logo and the colors of the logo in its design. You can see the logo on our website at www crestmore advisory. net.

```html
<!DOCTYPE html>
<html lang="en">
<head>
<meta charset="utf-8">
<title>Crestmore Advisory – Business Card</title>
<link rel="stylesheet" href="https://fonts.googleapis.com/css2?family=Montserrat:wght@400;500;700&display=swap">
<style>
  :root {
    --brand-blue: #0e5aa7;
    --accent-blue: #2ea6dc;
    --ink: #3a3a3a;
    --rule: #555555;
    --paper: #ffffff;
    --backdrop: #d9dde2;
  }
  * { box-sizing: border-box; margin: 0; padding: 0; }
  html, body {
    width: 1200px; height: 1000px; overflow: hidden;
    background: var(--backdrop);
    font-family: "Montserrat", sans-serif;
  }
  .card {
    position: absolute; left: 220px;
    width: 760px; height: 434px;
    border-radius: 26px; overflow: hidden;
  }
  .card-back {
    top: 40px;
    background: var(--brand-blue);
    display: flex; align-items: center; justify-content: center;
  }
  .card-back .brand-name {
    color: var(--paper); font-weight: 700;
    font-size: 64px; letter-spacing: 6px;
  }
  .card-front { top: 516px; background: var(--paper); }
  .brand-block {
    position: absolute; left: 40px; top: 120px; width: 300px;
    text-align: center;
  }
  .brand-block .brand-name {
    color: var(--brand-blue); font-weight: 700;
    font-size: 34px; letter-spacing: 2px; line-height: 1.1;
  }
  .brand-block .brand-sub {
    color: var(--brand-blue); font-weight: 700;
    font-size: 17px; letter-spacing: 3px; margin-top: 4px;
  }
  .divider {
    position: absolute; left: 372px; top: 105px;
    width: 1.5px; height: 190px; background: var(--rule);
  }
  .contact { position: absolute; left: 400px; top: 110px; color: var(--ink); }
  .person-name {
    font-weight: 700; font-size: 26px; letter-spacing: 3px;
    color: var(--accent-blue);
  }
  .person-name .surname { color: var(--brand-blue); }
  .person-title { font-size: 17px; margin: 2px 0 12px; letter-spacing: .5px; }
  .contact-row {
    display: flex; align-items: center; gap: 9px;
    font-size: 15.5px; line-height: 27px; letter-spacing: .5px;
  }
  .contact-row svg { width: 14px; height: 14px; fill: var(--brand-blue); flex: none; }
  .wave { position: absolute; left: 0; bottom: 0; width: 760px; height: 110px; }
  .wave path { fill: var(--brand-blue); }
  .address {
    position: absolute; left: 90px; bottom: 28px;
    color: var(--paper); font-size: 17px; letter-spacing: 1px;
  }
</style>
</head>
<body>
  <section class="card card-back">
    <span class="brand-name">CRESTMORE</span>
  </section>

  <section class="card card-front">
    <div class="brand-block">
      <div class="brand-name">CRESTMORE</div>
      <div class="brand-sub">ADVISORY LLC</div>
    </div>

    <div class="divider"></div>

    <div class="contact">
      <div class="person-name">DANIEL <span class="surname">HARLOW</span></div>
      <div class="person-title">General Manager</div>
      <div class="contact-row">
        <svg viewBox="0 0 24 24"><path d="M6.6 10.8a15.1 15.1 0 0 0 6.6 6.6l2.2-2.2c.3-.3.7-.4 1-.2 1.1.4 2.3.6 3.6.6.6 0 1 .4 1 1V20c0 .6-.4 1-1 1A17 17 0 0 1 3 4c0-.6.4-1 1-1h3.5c.6 0 1 .4 1 1 0 1.3.2 2.5.6 3.6.1.3 0 .7-.2 1z"/></svg>
        (555) 214-0187
      </div>
      <div class="contact-row">
        <svg viewBox="0 0 24 24"><path d="M7 1h10a2 2 0 0 1 2 2v18a2 2 0 0 1-2 2H7a2 2 0 0 1-2-2V3a2 2 0 0 1 2-2zm0 3v14h10V4zm5 15.5a1.2 1.2 0 1 0 0 2.4 1.2 1.2 0 0 0 0-2.4z"/></svg>
        (office) 555-362-4410
      </div>
      <div class="contact-row">
        <svg viewBox="0 0 24 24"><path d="M2 5h20v14H2zm2 2v.4l8 5.3 8-5.3V7zm0 2.8V17h16V9.8l-8 5.3z"/></svg>
        info@crestmoreadvisory.net
      </div>
      <div class="contact-row">
        <svg viewBox="0 0 24 24"><path d="M12 2a10 10 0 1 0 0 20 10 10 0 0 0 0-20zm6.9 6h-3a15 15 0 0 0-1.3-3.9A8 8 0 0 1 18.9 8zM12 4c.8 1.2 1.5 2.5 1.9 4h-3.8c.4-1.5 1.1-2.8 1.9-4zM4.3 14a8 8 0 0 1 0-4h3.4a16 16 0 0 0 0 4zm.8 2h3a15 15 0 0 0 1.3 3.9A8 8 0 0 1 5.1 16zm3-8h-3a8 8 0 0 1 4.3-3.9C8.8 5.3 8.4 6.6 8.1 8zM12 20c-.8-1.2-1.5-2.5-1.9-4h3.8c-.4 1.5-1.1 2.8-1.9 4zm2.3-6H9.7a14 14 0 0 1 0-4h4.6a14 14 0 0 1 0 4zm.3 5.9c.6-1.2 1-2.5 1.3-3.9h3a8 8 0 0 1-4.3 3.9zm1.7-5.9a16 16 0 0 0 0-4h3.4a8 8 0 0 1 0 4z"/></svg>
        www.crestmoreadvisory.net
      </div>
    </div>

    <svg class="wave" viewBox="0 0 760 110" preserveAspectRatio="none" aria-hidden="true">
      <path d="M0 0 C260 6 560 50 700 110 L0 110 Z"/>
    </svg>
    <div class="address">1450 W Alder street Fairview County name 4820</div>
  </section>
</body>
</html>
```